Design Challege - Simplify a Complex Message

We have a new website design, but one of the pages presents a particular problem.

Our company does ERP implementations. We have developed a proprietary approach to these implementations based on the idea that you must get eight (and only eight) things right. These eight things are listed below, summarized in one or two words each:

1. Value
2. Capability
3. Functionality
4. Data
5. Technology
6. Change Leadership
7. Quality
8. Governance

Each of these eight things can be summarized in a short paragraph, but when you combine all eight summaries with a brief introductory text, the result is a lot of text - so much text that the casual surfer may be overwhelmed by it.

The winning design will find an engaging way to present the information in a way that presents a high-level summary, using icons and one- or two-word descriptions above but revealing more information when clicked.

Our current design for this information, with a paragraph describing the eight elements in a table, is included as an upload in PDF and Microsoft Word formats. We are looking for a creative way to display these eight things, showing the detail only when the user wants to see it.

The website is being built in WordPress, using Elementor as a page builder.

We will implement (code) the page, but the winner will be asked to specify the widget or other add-in if one is required.

The design does not need to include a header or footer, we have those.

Target Market(s)

Business executives working in technology

Industry/Entity Type

Any

Number of Pages Required

1 page

Font styles to use
Sans Serif

Requirements
Must have
• A design for the body of the page, but not the header or footer.
Nice to have
• Unique icons or images appropriate for each of the eight things.
Should not have
• A lot of text on one page

```html
<!DOCTYPE html>
<html lang="en">
<head>
<meta charset="utf-8">
<title>ERP Implementations – Eight Things to Get Right</title>
<link href="https://fonts.googleapis.com/css2?family=Outfit:wght@300;400;500;600;700&display=swap" rel="stylesheet">
<style>
  :root {
    --navy: #0d3464;
    --cyan: #1ba8d8;
    --ink: #222a33;
    --body: #3d4550;
    --rule: #dfe3e8;
    --card: #ffffff;
    --page: #ffffff;
    --feature-top: #22aad6;
    --feature-bottom: #0d4c7e;
  }
  * { box-sizing: border-box; margin: 0; padding: 0; }
  html, body { width: 894px; height: 1200px; overflow: hidden; background: var(--page); }
  body { font-family: "Outfit", sans-serif; color: var(--ink); position: relative; }

  .intro { position: absolute; top: 40px; left: 0; width: 894px; text-align: center; }
  .intro__title { font-size: 24px; font-weight: 700; color: var(--navy); letter-spacing: -0.2px; line-height: 1.1; }
  .intro__bar { width: 42px; height: 1.5px; background: var(--ink); margin: 12px auto 10px; }
  .intro__subtitle { font-size: 11.5px; font-weight: 400; color: var(--cyan); margin-bottom: 8px; }
  .intro__text { font-size: 9.2px; line-height: 16.5px; color: var(--ink); width: 520px; margin: 0 auto; }
  .intro__text + .intro__text { margin-top: 3px; }

  .card {
    position: absolute; width: 216px; height: 282px; background: var(--card);
    box-shadow: 0 6px 22px rgba(20, 40, 70, 0.08);
  }
  .card__icon { position: absolute; left: 26px; top: 35px; width: 34px; height: 34px; color: var(--cyan); }
  .card__icon svg { width: 100%; height: 100%; fill: none; stroke: currentColor; stroke-width: 1.4; stroke-linecap: round; stroke-linejoin: round; }
  .card__title { position: absolute; left: 26px; top: 84px; font-size: 15.5px; font-weight: 600; color: var(--navy); }
  .card__rule { position: absolute; left: 24px; right: 0; top: 124px; height: 1px; background: var(--rule); }
  .card__text { position: absolute; left: 26px; top: 142px; width: 172px; font-size: 8.6px; font-weight: 300; line-height: 15.1px; color: var(--body); }
  .card__text li { list-style: none; padding-left: 8px; position: relative; }
  .card__text li::before { content: "•"; position: absolute; left: 0; }
  .card__more { position: absolute; left: 26px; top: 236px; display: flex; align-items: center; gap: 6px; font-size: 8.2px; font-weight: 500; color: var(--cyan); text-decoration: none; letter-spacing: 0.1px; }
  .card__more-dot { width: 12px; height: 12px; border-radius: 50%; background: var(--cyan); display: inline-flex; align-items: center; justify-content: center; }
  .card__more-dot svg { width: 6px; height: 6px; fill: none; stroke: #fff; stroke-width: 1.6; }

  .card--featured { background: linear-gradient(160deg, var(--feature-top) 0%, #1a82b4 50%, var(--feature-bottom) 100%); }
  .card--featured .card__photo { position: absolute; inset: 0; background: linear-gradient(160deg, rgba(34,170,214,0.0), rgba(13,76,126,0.35)); }
  .card--featured .card__icon, .card--featured .card__title, .card--featured .card__text, .card--featured .card__more { color: #fff; }
  .card--featured .card__rule { background: rgba(255,255,255,0.85); height: 1.5px; }
  .card--featured .card__more-dot { background: #fff; }
  .card--featured .card__more-dot svg { stroke: var(--cyan); }

  .pos-value { left: 105px; top: 204px; }
  .pos-capability { left: 340px; top: 204px; }
  .pos-functionality { left: 572px; top: 204px; }
  .pos-data { left: 105px; top: 508px; }
  .pos-technology { left: 340px; top: 508px; }
  .pos-change { left: 572px; top: 508px; }
  .pos-quality { left: 221px; top: 812px; }
  .pos-governance { left: 455px; top: 812px; }
</style>
</head>
<body>
  <header class="intro">
    <h1 class="intro__title">ERP Implementations</h1>
    <div class="intro__bar"></div>
    <p class="intro__subtitle">Eight Things to Get Right</p>
    <p class="intro__text">Like the roots and branches of a tree, there are many considerations in an ERP implementation. Focus too much on the minor details, and you can lose sight of the tree.</p>
    <p class="intro__text">In an ERP implementation, you must get eight major things right to be successful. Ignore any of them, and your implementation will fail. Get them right, and you will likely succeed.</p>
  </header>

  <article class="card card--featured pos-value">
    <div class="card__photo" role="img" aria-label="Photo of a business analytics dashboard on a screen, tinted blue"></div>
    <div class="card__icon"><svg viewBox="0 0 34 34"><rect x="2" y="26" width="3" height="5"/><rect x="8" y="23" width="3" height="8"/><rect x="14" y="20" width="3" height="11"/><rect x="20" y="16" width="3" height="15"/><rect x="26" y="11" width="3" height="20"/><path d="M2 21 L14 13 L22 9 L31 3"/><path d="M27 3 H31 V7"/><circle cx="13" cy="10" r="4.5"/><path d="M13 7.5 V12.5"/></svg></div>
    <h2 class="card__title">Value</h2>
    <div class="card__rule"></div>
    <p class="card__text">The project must provide value that significantly exceeds potential project costs and should be aligned with the company’s strategy. Its value and strategic alignment must be part</p>
    <a class="card__more" href="#value">LEARN MORE <span class="card__more-dot"><svg viewBox="0 0 6 6"><path d="M2 1 L4 3 L2 5"/></svg></span></a>
  </article>

  <article class="card pos-capability">
    <div class="card__icon"><svg viewBox="0 0 34 34"><path d="M11 5 L15 3 L19 5 L23 3"/><path d="M13 7 L17 5 L21 7"/><rect x="2" y="13" width="10" height="7" rx="1"/><path d="M4 16 H10 M4 18 H8"/><path d="M29 17 a3.5 3.5 0 1 0 -4 0 v3 h4 z"/><circle cx="17" cy="24" r="2.5"/><path d="M12 31 a5 4 0 0 1 10 0"/><path d="M17 20 V11 M15 13 L17 11 L19 13"/><path d="M8 23 L11 26 M27 23 L24 26"/></svg></div>
    <h2 class="card__title">Capability</h2>
    <div class="card__rule"></div>
    <div class="card__text"><p>The company and the implementation team must be capable of implementing the project on their own or with help. The project must have the following:</p><ul><li>Resources required, including people</li></ul></div>
    <a class="card__more" href="#capability">LEARN MORE <span class="card__more-dot"><svg viewBox="0 0 6 6"><path d="M2 1 L4 3 L2 5"/></svg></span></a>
  </article>

  <article class="card pos-functionality">
    <div class="card__icon"><svg viewBox="0 0 34 34"><circle cx="18" cy="11" r="7"/><circle cx="18" cy="11" r="3"/><path d="M18 2 V4 M18 18 V20 M9 11 H11 M25 11 H27 M12 5 L13.5 6.5 M22.5 15.5 L24 17 M24 5 L22.5 6.5"/><circle cx="25" cy="24" r="5"/><circle cx="25" cy="24" r="2"/><path d="M25 17.5 V19 M25 29 V30.5 M18.5 24 H20 M30 24 H31.5"/><circle cx="8" cy="25" r="4"/><circle cx="8" cy="25" r="1.5"/><path d="M8 19.5 V21 M8 29 V30.5 M2.5 25 H4 M12 25 H13.5"/></svg></div>
    <h2 class="card__title">Functionality</h2>
    <div class="card__rule"></div>
    <p class="card__text">An ERP project must support required business processes, both now and in the future. A systematic review of all business processes and how they will be supported, either</p>
    <a class="card__more" href="#functionality">LEARN MORE <span class="card__more-dot"><svg viewBox="0 0 6 6"><path d="M2 1 L4 3 L2 5"/></svg></span></a>
  </article>

  <article class="card pos-data">
    <div class="card__icon"><svg viewBox="0 0 34 34"><path d="M9 13 a4 4 0 0 1 1 -7.5 a6 6 0 0 1 11 -1 a4.5 4.5 0 0 1 4 8.5 z"/><circle cx="17" cy="9" r="2.5"/><ellipse cx="6" cy="19" rx="4.5" ry="2"/><path d="M1.5 19 V30 a4.5 2 0 0 0 9 0 V19 M1.5 23 a4.5 2 0 0 0 9 0 M1.5 26.5 a4.5 2 0 0 0 9 0"/><ellipse cx="17" cy="19" rx="4.5" ry="2"/><path d="M12.5 19 V30 a4.5 2 0 0 0 9 0 V19 M12.5 23 a4.5 2 0 0 0 9 0 M12.5 26.5 a4.5 2 0 0 0 9 0"/><ellipse cx="28" cy="19" rx="4.5" ry="2"/><path d="M23.5 19 V30 a4.5 2 0 0 0 9 0 V19 M23.5 23 a4.5 2 0 0 0 9 0 M23.5 26.5 a4.5 2 0 0 0 9 0"/></svg></div>
    <h2 class="card__title">Data</h2>
    <div class="card__rule"></div>
    <p class="card__text">ERP systems are data-hungry creatures. Please be careful before assuming that because so much data goes into them, an equal amount of insight will emerge. Getting data right</p>
    <a class="card__more" href="#data">LEARN MORE <span class="card__more-dot"><svg viewBox="0 0 6 6"><path d="M2 1 L4 3 L2 5"/></svg></span></a>
  </article>

  <article class="card pos-technology">
    <div class="card__icon"><svg viewBox="0 0 34 34"><path d="M18 4 a13 13 0 1 0 0 26"/><path d="M18 9 a8 8 0 1 0 0 16"/><path d="M18 2 V7 M18 27 V32 M6 8 L9 11 M6 26 L9 23 M2 17 H5"/><path d="M18 13 H26 M18 17 H31 M18 21 H26 M26 13 V9 H29 M26 21 V25 H29"/><circle cx="31" cy="17" r="1"/></svg></div>
    <h2 class="card__title">Technology</h2>
    <div class="card__rule"></div>
    <p class="card__text">What is the platform for the system? Is it offered by a vendor that will be around for as long as your system? Will it integrate with your other systems? Are resources available</p>
    <a class="card__more" href="#technology">LEARN MORE <span class="card__more-dot"><svg viewBox="0 0 6 6"><path d="M2 1 L4 3 L2 5"/></svg></span></a>
  </article>

  <article class="card pos-change">
    <div class="card__icon"><svg viewBox="0 0 34 34"><circle cx="17" cy="14" r="9"/><circle cx="17" cy="12" r="3.5"/><path d="M11 21 a6 5 0 0 1 12 0"/><circle cx="7" cy="24" r="2.5"/><path d="M2 32 a5 4 0 0 1 10 0"/><circle cx="27" cy="24" r="2.5"/><path d="M22 32 a5 4 0 0 1 10 0"/><circle cx="17" cy="2.5" r="1.2"/><circle cx="4" cy="9" r="1.2"/><circle cx="30" cy="9" r="1.2"/><path d="M14 28 L20 26"/></svg></div>
    <h2 class="card__title">Change Leadership</h2>
    <div class="card__rule"></div>
    <p class="card__text">Change leadership (often called change management) considers the human side of an ERP implementation. Change is hard, even if it’s a good change. Training is an important</p>
    <a class="card__more" href="#change-leadership">LEARN MORE <span class="card__more-dot"><svg viewBox="0 0 6 6"><path d="M2 1 L4 3 L2 5"/></svg></span></a>
  </article>

  <article class="card pos-quality">
    <div class="card__icon"><svg viewBox="0 0 34 34"><path d="M17 2 L25 5 V11 C25 16 21 19 17 21 C13 19 9 16 9 11 V5 Z"/><path d="M13 11 L16 14 L21 8"/><rect x="2" y="22" width="5" height="10"/><path d="M7 24 H12 C14 24 15 26 17 26 H21 M7 30 H19 L31 23 C32 21 30 20 28 21 L22 24"/></svg></div>
    <h2 class="card__title">Quality</h2>
    <div class="card__rule"></div>
    <p class="card__text">Quality is multi-dimensional, and it’s more than a measurement; it’s a perception. An ERP needs to be reliable. But poor performance or poor user experience are often root</p>
    <a class="card__more" href="#quality">LEARN MORE <span class="card__more-dot"><svg viewBox="0 0 6 6"><path d="M2 1 L4 3 L2 5"/></svg></span></a>
  </article>

  <article class="card pos-governance">
    <div class="card__icon"><svg viewBox="0 0 34 34"><circle cx="17" cy="11" r="8"/><path d="M17 1.5 V3 M17 19 V20.5 M7.5 11 H9 M25 11 H26.5"/><circle cx="14" cy="9" r="2"/><circle cx="20" cy="9" r="2"/><path d="M10.5 15 a3.5 3 0 0 1 7 0 M16.5 15 a3.5 3 0 0 1 7 0"/><path d="M2 20 L7 18 L11 27 L6 29 Z M32 20 L27 18 L23 27 L28 29 Z"/><path d="M9 21 L15 19 L21 22 M25 20 L19 26 C18 27 16 27 15 26 L10 25"/><path d="M15 23 L18 26 M13 24 L16 27"/></svg></div>
    <h2 class="card__title">Governance</h2>
    <div class="card__rule"></div>
    <p class="card__text">ERP projects require both management and leadership. Planning, changing plans, communication, decision making, and guidance are critical aspects of management.</p>
    <a class="card__more" href="#governance">LEARN MORE <span class="card__more-dot"><svg viewBox="0 0 6 6"><path d="M2 1 L4 3 L2 5"/></svg></span></a>
  </article>
</body>
</html>
```